Classic and neutral book cover design

We are looking for a classic and neutral book cover design to be used as the template for a series of books to be published. We are hence looking for a template that will allow us to easily change the title name for all books in this series.
The use of very few colours (black and white is welcome) and few design elements is a big bonus. As a source of inspiration we would like to ask you to view the very simple and
If you think you have a cool idea that can add a twist to the formal classic look don't hesitate. Go for it !
Work will be done for a 30 year old Sweden based cultural non-profit called VĂ©ru (www.veruhaus-example.org). We work with the publishing and supporting of post-modern art and literature addressing contemporary topics but are also involved in assisting projects of cultural preservation.
Target Market(s)
The audience is expected to have some form of interest in culture but could range from hobbyist readers to tenure track scholars
Industry/Entity Type
Non-Profit
Requirements
Must have
- General:
- Classic and neutral feel
- Preferably very simple and few shapes
- usage of few colours (black and white is welcome)
Information to be displayed on the cover is:
- Author
- Title
- type of work e.g. play/novel (optional)
- publishing house (in this case "Veru Publishing")
Nice to have
- ideas to prevent it from become boring are of course welcome
Should not have
- - too many colours

```html
<!DOCTYPE html>
<html lang="lv">
<head>
<meta charset="utf-8">
<title>Revidents — book cover</title>
<link rel="stylesheet" href="https://fonts.googleapis.com/css2?family=Arimo&family=Oswald:wght@400&display=swap">
<style>
  :root {
    --page: #efede8;
    --cover: #c8c1ad;
    --line: #e0ddd2;
    --ink: #5a5242;
  }
  html, body {
    margin: 0;
    width: 1200px;
    height: 1000px;
    overflow: hidden;
    background: var(--page);
  }
  .cover {
    position: absolute;
    left: 259px;
    top: 69px;
    width: 682px;
    height: 860px;
    background: var(--cover);
    box-shadow: 0 2px 4px rgba(0,0,0,0.18);
    overflow: hidden;
  }
  .cover-frames {
    position: absolute;
    inset: 0;
    width: 682px;
    height: 860px;
  }
  .cover-frames rect { fill: var(--line); }
  .cover-text {
    position: absolute;
    margin: 0;
    color: var(--ink);
    white-space: nowrap;
  }
  .author {
    left: 269px;
    top: 300px;
    font: 19px/1 "Arimo", Arial, sans-serif;
    letter-spacing: 0.2px;
  }
  .title {
    left: 268px;
    top: 385px;
    font: 400 36px/1 "Oswald", "Arial Narrow", sans-serif;
    letter-spacing: 1px;
    transform: scaleX(0.86);
    transform-origin: left top;
  }
  .genre {
    left: 321px;
    top: 421px;
    font: 18px/1 "Arimo", Arial, sans-serif;
  }
  .publisher {
    left: 272px;
    top: 562px;
    font: 19px/1 "Arimo", Arial, sans-serif;
    letter-spacing: 0.2px;
  }
</style>
</head>
<body>
  <div class="cover">
    <svg class="cover-frames" viewBox="259 69 682 860" aria-hidden="true">
      <!-- upper frame -->
      <rect x="480" y="92" width="251" height="13"/>
      <rect x="480" y="92" width="9" height="801"/>
      <rect x="721" y="92" width="10" height="329"/>
      <!-- large frame -->
      <rect x="357" y="145" width="503" height="26"/>
      <rect x="357" y="145" width="20" height="642"/>
      <rect x="840" y="145" width="20" height="642"/>
      <rect x="357" y="762" width="503" height="25"/>
      <!-- title frame -->
      <rect x="489" y="308" width="298" height="15"/>
      <rect x="489" y="308" width="12" height="403"/>
      <rect x="775" y="308" width="12" height="403"/>
      <rect x="489" y="695" width="298" height="16"/>
      <rect x="489" y="421" width="351" height="20"/>
      <!-- lower frame -->
      <rect x="480" y="787" width="14" height="106"/>
      <rect x="843" y="787" width="15" height="106"/>
      <rect x="480" y="875" width="378" height="18"/>
      <!-- left edge frame -->
      <rect x="259" y="181" width="11" height="734"/>
      <rect x="270" y="602" width="62" height="21"/>
      <rect x="316" y="602" width="16" height="327"/>
    </svg>
    <p class="cover-text author">Aleksandrs Morvis</p>
    <h1 class="cover-text title">REVIDENTS</h1>
    <p class="cover-text genre">luga</p>
    <p class="cover-text publisher">Veru Publishing</p>
  </div>
</body>
</html>
```